Flyer-Design für den Bereich Familienfotografie
Helene hat hervorragende Arbeit geleistet. Der erste Wurf war schon überzeugend. Änderungswünsche zum finalen Design wurden schnell und gut umgesetzt und besonders gefallen haben mir die von ihr proaktiv eingebrachten Ideen und Lösungsvorschläge. Vielen Dank!
Zielgruppe
Ich bin ein Fotograf mit dem Schwerpunkt Familienfotos und Reportagen
Aufgabenstellung
Hier soll ein Flyer für den Bereich Familienfotografie entstehen. Also Schwangerschaft, Baby, Familien, Portrait & Pärchen. Er soll Infos zu meinem Leistungsumfang und zum Ablauf von Buchungen, Shootings und Bildauswahl transtportieren. Hier gerne erstmal Blindtext vorsehen, ich liefere dann Inhalt nach.
Infos und weitere Eindrücke gibts auf www.bernhardlossow.de
Die beigefügten Bilder müssen natürlich nicht alle genutzt werden, vor Erstellung der Druckdaten suche ich die Bilder auch noch ohne Logo und in einer höheren Auflösung heraus, zur Gestaltung sollte das aber reichen.
Als Format wäre Din lang hochkant mit 6-8 Seiten ganz schön, (wegen Postversand im Brief/Rechnungsumschlag). Wenn Ihr gute Gründe für anderes liefert, lassen ich mich aber sicher auch überzeugen.
Optisch soll der Flyer schon auffallen, also etwas mehr als ein paar Fotos und Text drauffallen lassen, bitte aber kein verschnörkelter pastell 'Schi-Schi' wie er immer mal wieder aus dem anglophonen Raum zu uns schwappt ;)
Ich freue mich auf Eure Ideen!
Im Nachgang zu diesem Projekt sollen dann auf der Basis noch Flyer für Hochzeiten und Reportagen erstellt werden, sowie in 2019 auch neue Visitenkarten und ein Portfolio-Booklet. Diese Aufträge gehen dann natürlich auch an den oder diejenige, die sich bei dem 'Familienflyer' durchsetzt.
Falls Fragen oder Unklarheiten aufkommen, lasst es mich gerne wissen! Kontaktdaten findet Ihr auf meiner Seite.
Generell habe ich mich vielleicht noch nicht klar genug ausgedrückt (sorry, ist mein erstes Projekt hier)
Der Flyer soll natürlich die Wertigkeit und Professionalität meiner Arbeit widerspiegeln. Ganz klar soll er NICHT so aussehen, als hätte man das Ganze in 3 min in Powerpoint zusammengeklickt.
Es muss direkt klar werden, dass es in dem Flyer um die Familienfotografie geht und es sollen alle 4 Bereiche (Schwangerschaft, Baby, Familien, Portraits/Pärchen) darges..

```html
<!DOCTYPE html>
<html lang="de">
<head>
<meta charset="utf-8">
<title>Familienfotografie – Leistungen</title>
<link href="https://fonts.googleapis.com/css2?family=Arimo:wght@400;700&display=swap" rel="stylesheet">
<style>
  :root {
    --band: #454545;
    --ink: #111111;
    --panel: #000000;
    --paper: #ffffff;
    --body: #2b2b2b;
  }
  html, body { margin: 0; padding: 0; overflow: hidden; }
  body { width: 1200px; height: 927px; background: var(--paper); font-family: "Arimo", Arial, sans-serif; }
  .flyer { position: relative; width: 1200px; height: 927px; overflow: hidden; background: var(--paper); }
  .band-top { position: absolute; left: 0; top: 0; width: 1200px; height: 36px; background: var(--band); }
  .band-bottom { position: absolute; left: 400px; top: 895px; width: 800px; height: 32px; background: var(--band); }
  .hero { position: absolute; left: 0; top: 36px; width: 799px; height: 456px;
    background: radial-gradient(ellipse at 35% 45%, #b89a8a 0%, #6b5a55 35%, #2a2420 70%, #120f0a 100%); }
  .about { position: absolute; left: 0; top: 492px; width: 400px; height: 435px; background: var(--panel); color: var(--paper); text-align: center; }
  .about-photo { position: absolute; left: 121px; top: 20px; width: 164px; height: 164px; border-radius: 50%;
    background: radial-gradient(circle at 50% 40%, #9a7a6a 0%, #4a4650 55%, #1e1e24 100%); }
  .about-text { position: absolute; left: 30px; top: 188px; width: 340px; margin: 0; font-size: 15.3px; line-height: 20.7px; }
  .about-quote { position: absolute; left: 0; top: 374px; width: 400px; margin: 0; font-size: 15.3px; }
  .services-title { position: absolute; left: 904px; top: 82px; margin: 0; padding-left: 17px; border-left: 5px solid var(--ink);
    font-size: 28px; font-weight: 700; line-height: 30px; color: var(--ink); }
  .service-photo { position: absolute; width: 157px; height: 157px; border-radius: 50%; }
  .service-name { position: absolute; margin: 0; font-size: 23px; font-weight: 700; color: var(--ink); line-height: 26px; }
  .service-rule { position: absolute; height: 4px; background: var(--ink); }
  .service-text { position: absolute; width: 166px; margin: 0; font-size: 10.8px; line-height: 15.3px; color: var(--body); word-break: break-all; }
</style>
</head>
<body>
<div class="flyer">
  <div class="band-top"></div>
  <div class="hero" role="img" aria-label="Foto: lachendes Mädchen mit ihrem Vater vor dunklem Hintergrund"></div>

  <section class="about">
    <div class="about-photo" role="img" aria-label="Porträt des Fotografen mit Kamera"></div>
    <p class="about-text">Ob nun im Studio oder draußen in der Natur in Wiesbrück, dem Weidenland und Umgebung, jedes Shooting ist einzigartig und es braucht Kreativität, Spontanität, Einfühlungsvermögen und ein waches Auge. Genau das mag ich an meiner Arbeit, wenn ich dann den Auslöser drücke, und mir das vertraute Klacken der Kamera sagt:</p>
    <p class="about-quote">„ ... Bild im Kasten“</p>
  </section>

  <h2 class="services-title">Leistungen</h2>

  <div class="service-photo" style="left:831px;top:150px;background:radial-gradient(circle at 45% 40%,#d8c0b0 0%,#6a4a8a 35%,#8fae6a 70%,#dfe8d8 100%);" role="img" aria-label="Foto: Frau im lila Kleid auf einer Wiese"></div>
  <h3 class="service-name" style="left:1008px;top:174px;">Portrait</h3>
  <div class="service-rule" style="left:1007px;top:200px;width:108px;"></div>
  <p class="service-text" style="left:1008px;top:219px;">BlindtextBlindtextBlindtextBlindtextBlindtextBlindtextBlindtextBlindtextBlindtextBlindtextBlindtextBlindtextBlindtextBlindtextBlindtextBlindtextBlindtextBlindtextBlindtextBlindtextBlindtextBlindtext</p>

  <div class="service-photo" style="left:831px;top:396px;background:linear-gradient(180deg,#7a8a90 0%,#4a6a8a 45%,#e8e2d8 65%,#a07a4a 100%);" role="img" aria-label="Foto: schlafendes Baby in einem Weidenkorb"></div>
  <h3 class="service-name" style="left:1007px;top:417px;">Familie</h3>
  <div class="service-rule" style="left:1007px;top:442px;width:140px;"></div>
  <p class="service-text" style="left:1008px;top:464px;">BlindtextBlindtextBlindtextBlindtextBlindtextBlindtextBlindtextBlindtextBlindtextBlindtextBlindtextBlindtextBlindtextBlindtextBlindtextBlindtextBlindtextBlindtextBlindtextBlindtextBlindtextBlindtext</p>

  <div class="service-photo" style="left:831px;top:652px;background:linear-gradient(180deg,#cfe0f0 0%,#f4f6f8 40%,#9ab870 70%,#4f7a3a 100%);" role="img" aria-label="Foto: Paar auf einer sonnigen Sommerwiese"></div>
  <h3 class="service-name" style="left:1007px;top:677px;">Paar-Shootings</h3>
  <div class="service-rule" style="left:1007px;top:706px;width:138px;"></div>
  <p class="service-text" style="left:1008px;top:724px;">BlindtextBlindtextBlindtextBlindtextBlindtextBlindtextBlindtextBlindtextBlindtextBlindtextBlindtextBlindtextBlindtextBlindtextBlindtextBlindtextBlindtextBlindtextBlindtextBlindtextBlindtextBlindtext</p>

  <div class="service-photo" style="left:522px;top:552px;background:radial-gradient(circle at 60% 55%,#e8c8b0 0%,#f4f2f0 45%,#ffffff 70%,#3a3a3a 100%);" role="img" aria-label="Foto: Babybauch einer Schwangeren mit weißer Bluse"></div>
  <h3 class="service-name" style="left:500px;top:719px;width:200px;text-align:center;">Schwangerschaft</h3>
  <div class="service-rule" style="left:529px;top:757px;width:141px;"></div>
  <p class="service-text" style="left:517px;top:778px;">BlindtextBlindtextBlindtextBlindtextBlindtextBlindtextBlindtextBlindtextBlindtextBlindtextBlindtextBlindtextBlindtextBlindtextBlindtextBlindtextBlindtextBlindtextBlindtextBlindtextBlindtextBlindtext</p>

  <div class="band-bottom"></div>
</div>
</body>
</html>
```